Dential Clinic Business Card

We need a simple elegant business card. 2 sided. First side with our details, and 2nd side with appointment time rows.

Dark background preferred. Will consider monotone design, or colored. Surprise us.

Details:
SIDE1

Harwick Plaza Dental

Dr Milo Brent
BDSc(Tarn) MOPRVS

Shop 42, Harwick Plaza
8-22 Larch Avenue, Croydon VIC 3136
Phone: 03 9447 2835
email: info@harwickplazadental.com.au
site: www.harwickplazadental.com.au
_____________________________________
SIDE 2
Appointed Time ________________________
Notes _______________________

Target Market(s)

Dental Patients

Industry/Entity Type

Healthcare

Contact Information for Business Card

SIDE1

Harwick Plaza Dental

Dr Milo Brent
Shop 42, Harwick Plaza
Phone: 03 9447 2835
SIDE 2

Font styles to use
Other font styles liked:
• Comfortaa

Requirements
Must have
• Dr Milo Brent
BDSc(Tarn) MOPRVS

Address
Phone
Email
Website
Nice to have
• Simple elegant design with our logo.
Colored logo.
Light text on dark background - Side 1
Light background so can be written on with dark pen - SIde 2
Should not have
• Too many colors

```html
<!DOCTYPE html>
<html lang="en">
<head>
<meta charset="utf-8">
<title>Harwick Plaza Dental – Business Card</title>
<link href="https://fonts.googleapis.com/css2?family=Questrial&display=swap" rel="stylesheet">
<style>
  :root {
    --bg: #5d5f60;
    --card-dark: #1c1c1c;
    --paper: #ffffff;
    --blue: #1e98d6;
    --green: #7cc242;
    --ink: #1a1a1a;
    --grey-text: #9a9a9a;
    --light-text: #d8d8d8;
  }
  * { box-sizing: border-box; margin: 0; padding: 0; }
  html, body {
    width: 1200px; height: 965px; overflow: hidden;
    background: var(--bg);
    font-family: "Questrial", "Century Gothic", sans-serif;
  }
  .sheet {
    width: 1200px; height: 965px;
    display: flex; flex-direction: column; align-items: center; justify-content: center;
    gap: 40px;
  }
  .card {
    width: 680px; height: 416px;
    position: relative; overflow: hidden;
    box-shadow: 0 8px 24px rgba(0,0,0,.35);
  }

  /* Appointment side */
  .appointment { background: var(--paper); }
  .appointment__header {
    height: 130px; background: var(--card-dark);
    display: flex; align-items: center; padding-left: 60px; gap: 16px;
  }
  .brand__dot {
    width: 34px; height: 34px; border-radius: 50%; background: var(--green);
  }
  .brand__name {
    color: var(--green); font-size: 38px; letter-spacing: 1px; text-transform: uppercase;
    white-space: nowrap;
  }
  .appointment__rule {
    position: absolute; left: 60px; right: 40px; top: 152px;
    height: 1.5px; background: var(--green);
  }
  .appointment__rows {
    position: absolute; left: 60px; right: 40px; top: 188px;
    display: flex; flex-direction: column; gap: 24px;
  }
  .row { display: flex; align-items: flex-end; gap: 10px; height: 28px; }
  .row__label { color: var(--blue); font-size: 20px; text-transform: uppercase; white-space: nowrap; }
  .row__line { flex: 1; border-bottom: 1.5px solid var(--ink); margin-bottom: 4px; }

  /* Details side */
  .details { background: var(--card-dark); }
  .details__main {
    position: absolute; left: 36px; right: 30px; top: 130px;
    display: flex; align-items: center; justify-content: center; gap: 20px;
  }
  .dentist { text-align: right; flex: none; }
  .dentist__name {
    color: var(--blue); font-size: 40px; font-weight: 400; text-transform: uppercase;
    letter-spacing: 1px; line-height: 1; white-space: nowrap;
  }
  .dentist__title { color: var(--grey-text); font-size: 18px; margin-top: 8px; white-space: nowrap; }
  .dentist__quals { color: var(--grey-text); font-size: 15px; margin-top: 4px; white-space: nowrap; }
  .divider { width: 1.5px; height: 100px; background: var(--blue); flex: none; }
  .contact { list-style: none; display: flex; flex-direction: column; gap: 8px; flex: none; }
  .contact__item {
    display: flex; align-items: center; gap: 9px;
    color: var(--light-text); font-size: 14px; white-space: nowrap;
  }
  .contact__icon { width: 16px; height: 16px; flex: none; }
  .contact__accent { color: var(--green); }
  .address-band {
    position: absolute; left: 0; right: 0; bottom: 0; height: 54px;
    background: var(--green); color: var(--ink);
    display: flex; align-items: center; justify-content: center;
    font-size: 19px; white-space: nowrap;
  }
</style>
</head>
<body>
<main class="sheet">

  <section class="card appointment" aria-label="Appointment side">
    <header class="appointment__header">
      <span class="brand__dot"></span>
      <span class="brand__name">Harwick Plaza Dental</span>
    </header>
    <div class="appointment__rule"></div>
    <div class="appointment__rows">
      <div class="row"><span class="row__label">Appointed Time:</span><span class="row__line"></span></div>
      <div class="row"><span class="row__label">Notes:</span><span class="row__line"></span></div>
      <div class="row"><span class="row__label">Appointed Time:</span><span class="row__line"></span></div>
      <div class="row"><span class="row__label">Notes:</span><span class="row__line"></span></div>
    </div>
  </section>

  <section class="card details" aria-label="Details side">
    <div class="details__main">
      <div class="dentist">
        <h1 class="dentist__name">Dr Milo Brent</h1>
        <p class="dentist__title">Principal Dentist</p>
        <p class="dentist__quals">BDSc(Tarn) MOPRVS</p>
      </div>
      <div class="divider"></div>
      <ul class="contact">
        <li class="contact__item">
          <svg class="contact__icon" viewBox="0 0 24 24" fill="none" stroke="#7cc242" stroke-width="2" stroke-linecap="round" stroke-linejoin="round"><path d="M5 3h4l2 5-2.5 1.5a11 11 0 0 0 6 6L16 13l5 2v4a2 2 0 0 1-2 2A16 16 0 0 1 3 5a2 2 0 0 1 2-2z"/></svg>
          03 9447 2835
        </li>
        <li class="contact__item">
          <svg class="contact__icon" viewBox="0 0 24 24" fill="none" stroke="#7cc242" stroke-width="2" stroke-linejoin="round"><rect x="3" y="5" width="18" height="14" rx="1"/><path d="M3 6l9 7 9-7"/></svg>
          info@harwickplazadental.com.au
        </li>
        <li class="contact__item">
          <svg class="contact__icon" viewBox="0 0 24 24" fill="none" stroke="#7cc242" stroke-width="2"><circle cx="12" cy="12" r="9"/><path d="M3 12h18M12 3c3 3 3 15 0 18M12 3c-3 3-3 15 0 18"/></svg>
          <span>www.<span class="contact__accent">harwickplazadental</span>.com.au</span>
        </li>
      </ul>
    </div>
    <footer class="address-band">Shop 42, Harwick Plaza, 8-22 Larch Avenue, Croydon VIC 3136</footer>
  </section>

</main>
</body>
</html>
```